Bref créative
Overseas Capital Partners
I need single sided standard sized Business Card [3.5" x 2"]
May be same as in logo, may be another
Professional
Marek Dobrzyn
Manager
ul. Lipowa 17
41-806 Katowice
Poland
marek.dobrzyn@korvant.com.pl
www.korvant.com.pl

```html
<!DOCTYPE html>
<html lang="en">
<head>
<meta charset="utf-8">
<title>Korvant – Business Cards</title>
<link rel="stylesheet" href="https://fonts.googleapis.com/css2?family=Source+Sans+3:wght@400;600&display=swap">
<style>
  :root {
    --page: #ffffff;
    --card-light: #ffffff;
    --card-dark: #000000;
    --brand-blue: #00a6e6;
    --brand-sky: #5cc4ef;
    --line-sky: #8fd6f5;
    --ink-dark: #1a1a1a;
    --ink-light: #ffffff;
    --edge: #b5b5b5;
  }
  html, body {
    margin: 0;
    width: 1200px;
    height: 909px;
    overflow: hidden;
    background: var(--page);
    font-family: "Source Sans 3", "Myriad Pro", Arial, sans-serif;
  }
  .canvas { position: relative; width: 1200px; height: 909px; }
  .card { position: absolute; display: block; }
  .card--light { left: 29px; top: 67px; width: 684px; height: 370px; }
  .card--dark  { left: 451px; top: 456px; width: 701px; height: 384px; }
  .brand-name { font-weight: 400; letter-spacing: 11px; fill: var(--brand-sky); }
  .person-name { font-weight: 400; }
  .person-role { font-weight: 400; }
  .contact { font-weight: 400; fill: var(--ink-light); }
  .on-light { fill: var(--ink-dark); }
  .on-dark { fill: var(--ink-light); }
</style>
</head>
<body>
<main class="canvas">

  <svg class="card card--light" viewBox="0 0 684 370" aria-label="Business card, light version">
    <rect class="card-base" x="0.5" y="0.5" width="683" height="369" fill="var(--card-light)" stroke="var(--edge)"/>
    <circle class="brand-mark" cx="342" cy="80" r="38" fill="var(--brand-sky)"/>
    <text class="brand-name" x="347" y="174" text-anchor="middle" font-size="40">KORVANT</text>
    <text class="person-name on-light" x="342" y="212" text-anchor="middle" font-size="29">Marek Dobrzyn</text>
    <text class="person-role on-light" x="342" y="237" text-anchor="middle" font-size="16">Manager</text>
    <path class="accent-line" d="M0,204 Q342,300 684,204" fill="none" stroke="var(--line-sky)" stroke-width="3"/>
    <path class="contact-band" d="M0,220 Q342,318 684,220 L684,370 L0,370 Z" fill="var(--brand-blue)"/>
    <text class="contact" x="342" y="288" text-anchor="middle" font-size="17">ul. Lipowa 17, 41-806 Katowice, Poland</text>
    <text class="contact" x="342" y="312" text-anchor="middle" font-size="17">Cell: +48 512 73 40 86</text>
    <text class="contact" x="342" y="336" text-anchor="middle" font-size="17">Email: marek.dobrzyn@korvant.com.pl | www.korvant.com.pl</text>
  </svg>

  <svg class="card card--dark" viewBox="0 0 701 384" aria-label="Business card, dark version">
    <rect class="card-base" x="0" y="0" width="701" height="384" fill="var(--card-dark)"/>
    <circle class="brand-mark" cx="350" cy="90" r="40" fill="var(--brand-sky)"/>
    <text class="brand-name" x="356" y="190" text-anchor="middle" font-size="42">KORVANT</text>
    <text class="person-name on-dark" x="350" y="229" text-anchor="middle" font-size="29">Marek Dobrzyn</text>
    <text class="person-role on-dark" x="350" y="254" text-anchor="middle" font-size="16">Manager</text>
    <path class="accent-line" d="M0,222 Q350,312 701,222" fill="none" stroke="var(--line-sky)" stroke-width="3"/>
    <path class="contact-band" d="M0,238 Q350,330 701,238 L701,384 L0,384 Z" fill="var(--brand-blue)"/>
    <text class="contact" x="350" y="318" text-anchor="middle" font-size="17">ul. Lipowa 17, 41-806 Katowice, Poland</text>
    <text class="contact" x="350" y="342" text-anchor="middle" font-size="17">Cell: +48 512 73 40 86</text>
    <text class="contact" x="350" y="366" text-anchor="middle" font-size="17">Email: marek.dobrzyn@korvant.com.pl | www.korvant.com.pl</text>
  </svg>

</main>
</body>
</html>
```